WordPress Site That Reviews Footwear

We need a wordpress web design for an affiliate site called TarnWisp. We review and do roundups on footwear products. The final design should be clean and mobile friendly. The site should be built with Gutenberg page builder. We like the design of https://petalharvin.com/.

Target Market(s)

USA

Industry/Entity Type

Footwear

Logo Text

TarnWisp

Number of Pages Required

4 page

Font styles to use
Serif
Sans Serif

Requirements
Must have
• Wordpress site
Blog post
Page
Categories
Homepage

```html
<!DOCTYPE html>
<html lang="en">
<head>
<meta charset="utf-8">
<title>TarnWisp – Archives</title>
<link href="https://fonts.googleapis.com/css2?family=Playfair+Display:wght@400;700;900&family=Poppins:wght@400;500;600&display=swap" rel="stylesheet">
<style>
:root{
  --ink:#1f1f1f;
  --text:#555;
  --muted:#888;
  --accent:#e84a2a;
  --red:#e0302f;
  --line:#e6e6e6;
  --footer:#f4f4f4;
  --white:#fff;
}
*{box-sizing:border-box;margin:0;padding:0}
html,body{width:1200px;height:2250px;overflow:hidden;background:var(--white);font-family:'Poppins',sans-serif;color:var(--ink)}
.page{position:relative;width:1200px;height:2250px}
.header{position:absolute;top:0;left:0;width:1200px;height:93px;display:flex;align-items:center;padding:0 88px;font-size:12px;font-weight:600;letter-spacing:.2px}
.nav{display:flex;gap:26px}
.nav span small{font-size:8px;margin-left:2px}
.logo{position:absolute;left:0;right:0;text-align:center;font-family:'Playfair Display',serif;font-size:31px;font-weight:400;pointer-events:none}
.nav-right{margin-left:auto;display:flex;gap:26px;align-items:center}
.icons{display:flex;gap:18px;margin-left:44px;align-items:center}
.cart{position:relative}
.badge{position:absolute;top:-8px;right:-8px;width:14px;height:14px;border-radius:50%;background:var(--red);color:#fff;font-size:9px;display:flex;align-items:center;justify-content:center}
.hero{position:absolute;top:93px;left:0;width:1200px;height:323px;background:linear-gradient(90deg,#5c5b59 0%,#5a5957 45%,#3a3a3c 62%,#56555a 80%,#6a6866 100%)}
.hero-title{position:absolute;left:88px;top:110px;font-family:'Playfair Display',serif;font-size:62px;font-weight:400;color:#fff;line-height:1}
.hero-sub{position:absolute;left:88px;top:178px;width:360px;font-size:14px;line-height:20px;color:#fff}
.sec-title{position:absolute;font-family:'Playfair Display',serif;font-size:32px;font-weight:400;line-height:1}
.sec-title b{font-weight:900}
.sec-title::after{content:"";position:absolute;left:1px;top:44px;width:30px;height:2px;background:var(--red)}
.rule{position:absolute;height:1px;background:var(--line)}
.article{position:absolute;left:88px;width:700px;height:185px}
.thumb{position:absolute;left:0;top:0;width:281px;height:185px;border-radius:3px}
.meta{position:absolute;left:311px;top:16px;font-size:11px;color:var(--muted);font-weight:500}
.meta i{display:inline-block;width:4px;height:4px;border-radius:50%;background:#ccc;margin:0 6px 2px;vertical-align:middle}
.a-title{position:absolute;left:311px;top:36px;font-family:'Playfair Display',serif;font-size:24px;font-weight:700;white-space:nowrap}
.a-text{position:absolute;left:311px;top:77px;width:385px;font-size:14px;line-height:20.5px;color:var(--text)}
.read{position:absolute;left:311px;top:154px;font-size:10.5px;font-weight:600;display:flex;align-items:center;gap:6px}
.topics{position:absolute;left:856px;top:599px;width:254px;list-style:none}
.topics li{height:53.4px;display:flex;align-items:center;justify-content:space-between;font-size:13px;border-bottom:1px dashed var(--line)}
.topics li:last-child{border-bottom:none}
.pager{position:absolute;left:87px;top:1713px;display:flex;align-items:center;gap:14px;font-size:19px}
.pager .pg{width:46px;height:46px;border-radius:50%;display:flex;align-items:center;justify-content:center}
.pager .arrow{background:#eee}
.pager .active{background:var(--accent);color:#fff}
.footer{position:absolute;top:1851px;left:0;width:1200px;height:399px;background:var(--footer)}
.fcol{position:absolute;top:76px}
.fcol h4{font-family:'Playfair Display',serif;font-size:19px;font-weight:700;margin-bottom:14px}
.fcol a{display:block;font-size:13px;color:var(--text);line-height:26.7px;text-decoration:none}
.contact-row{display:flex;gap:10px;font-size:13px;color:var(--text);line-height:18px;margin-bottom:10px}
.contact-row svg{flex:none;margin-top:2px}
.socials{display:flex;gap:8px;margin-bottom:34px}
.socials span{width:31px;height:31px;border-radius:50%}
.pay{display:flex;gap:10px}
.pay span{width:49px;height:32px;border-radius:4px;display:flex;align-items:center;justify-content:center;font-size:8.5px;font-weight:600}
.f-rule{position:absolute;left:92px;width:1022px;top:344px;height:1px;background:#d8d8d8}
.copy{position:absolute;top:364px;left:0;width:1200px;text-align:center;font-size:12.5px;font-weight:600}
.totop{position:absolute;left:1134px;top:324px;width:41px;height:41px;border-radius:50%;background:var(--red);display:flex;align-items:center;justify-content:center}
</style>
</head>
<body>
<div class="page">
  <header class="header">
    <nav class="nav">
      <span>MEN<small>▾</small></span><span>WOMEN<small>▾</small></span><span>KIDS<small>▾</small></span><span>FAVORITES</span><span>CUSTOMIZE</span>
    </nav>
    <div class="logo">TarnWisp</div>
    <div class="nav-right">
      <span>ABOUT</span><span>CONTACT US</span>
      <div class="icons">
        <svg width="20" height="20" viewBox="0 0 20 20" fill="none" stroke="#222" stroke-width="1.5"><circle cx="10" cy="6" r="4.5"/><path d="M2 19c0-5 3.5-8 8-8s8 3 8 8"/></svg>
        <svg width="20" height="20" viewBox="0 0 20 20" fill="none" stroke="#222" stroke-width="1.6"><circle cx="8.5" cy="8.5" r="6.5"/><path d="M13.5 13.5L19 19"/></svg>
        <span class="cart"><svg width="22" height="20" viewBox="0 0 22 20" fill="none" stroke="#222" stroke-width="1.5"><path d="M1 2h3l3 11h11l2-8H6"/><circle cx="8.5" cy="17.5" r="1.5"/><circle cx="16.5" cy="17.5" r="1.5"/></svg><span class="badge">0</span></span>
      </div>
    </div>
  </header>

  <section class="hero" role="img" aria-label="Photo of crossed legs wearing black sneakers with coral laces on a grey floor">
    <h1 class="hero-title">Archives</h1>
    <p class="hero-sub">Aenean sollicitudin lorem quis bibendum auctor amet nibh vulputate dummy...</p>
  </section>

  <h2 class="sec-title" style="left:88px;top:503px">Our Latest <b>Articles</b></h2>
  <div class="rule" style="left:88px;top:572px;width:636px"></div>
  <h2 class="sec-title" style="left:856px;top:503px">Related <b>Topics</b></h2>
  <div class="rule" style="left:856px;top:572px;width:254px"></div>

  <article class="article" style="top:600px">
    <div class="thumb" role="img" aria-label="Navy sneakers hanging by laces on pink background" style="background:linear-gradient(135deg,#f3bfd6,#eeb0cc)"></div>
    <div class="meta">By John<i></i>January 2021</div>
    <h3 class="a-title">Some Blog Heading Goes Here</h3>
    <p class="a-text">Duis sed odio sit amet nibh vulputate cursus a sit amet mauris morbi accumsain ipsum velit nam tellus a odio tincidunt auctor a ornare odio...</p>
    <div class="read">READ <svg width="12" height="8" viewBox="0 0 12 8" fill="none" stroke="#222" stroke-width="1.2"><path d="M0 4h11M8 1l3 3-3 3"/></svg></div>
  </article>
  <article class="article" style="top:820px">
    <div class="thumb" role="img" aria-label="Black high heels on a cream background" style="background:linear-gradient(135deg,#fbe7c8,#f6dcb8)"></div>
    <div class="meta">By John<i></i>January 2021</div>
    <h3 class="a-title">Some Blog Heading Goes Here</h3>
    <p class="a-text">Duis sed odio sit amet nibh vulputate cursus a sit amet mauris morbi accumsain ipsum velit nam tellus a odio tincidunt auctor a ornare odio...</p>
    <div class="read">READ <svg width="12" height="8" viewBox="0 0 12 8" fill="none" stroke="#222" stroke-width="1.2"><path d="M0 4h11M8 1l3 3-3 3"/></svg></div>
  </article>
  <article class="article" style="top:1040px">
    <div class="thumb" role="img" aria-label="White slip-on shoes on a beige background" style="background:linear-gradient(135deg,#d4bea2,#c9b294)"></div>
    <div class="meta">By John<i></i>January 2021</div>
    <h3 class="a-title">Some Blog Heading Goes Here</h3>
    <p class="a-text">Duis sed odio sit amet nibh vulputate cursus a sit amet mauris morbi accumsain ipsum velit nam tellus a odio tincidunt auctor a ornare odio...</p>
    <div class="read">READ <svg width="12" height="8" viewBox="0 0 12 8" fill="none" stroke="#222" stroke-width="1.2"><path d="M0 4h11M8 1l3 3-3 3"/></svg></div>
  </article>
  <article class="article" style="top:1260px">
    <div class="thumb" role="img" aria-label="Brown suede baby moccasins on a light grey background" style="background:linear-gradient(135deg,#ecebea,#e2e0de)"></div>
    <div class="meta">By John<i></i>January 2021</div>
    <h3 class="a-title">Some Blog Heading Goes Here</h3>
    <p class="a-text">Duis sed odio sit amet nibh vulputate cursus a sit amet mauris morbi accumsain ipsum velit nam tellus a odio tincidunt auctor a ornare odio...</p>
    <div class="read">READ <svg width="12" height="8" viewBox="0 0 12 8" fill="none" stroke="#222" stroke-width="1.2"><path d="M0 4h11M8 1l3 3-3 3"/></svg></div>
  </article>
  <article class="article" style="top:1480px">
    <div class="thumb" role="img" aria-label="White slippers on a pink and yellow background" style="background:linear-gradient(135deg,#f4c6c6 50%,#ece58e 50%)"></div>
    <div class="meta">By John<i></i>January 2021</div>
    <h3 class="a-title">Some Blog Heading Goes Here</h3>
    <p class="a-text">Duis sed odio sit amet nibh vulputate cursus a sit amet mauris morbi accumsain ipsum velit nam tellus a odio tincidunt auctor a ornare odio...</p>
    <div class="read">READ <svg width="12" height="8" viewBox="0 0 12 8" fill="none" stroke="#222" stroke-width="1.2"><path d="M0 4h11M8 1l3 3-3 3"/></svg></div>
  </article>

  <ul class="topics">
    <li>FLIP-FLOPS <svg width="13" height="8" viewBox="0 0 13 8" fill="none" stroke="#222" stroke-width="1.1"><path d="M0 4h12M9 1l3 3-3 3"/></svg></li>
    <li>SANDALS <svg width="13" height="8" viewBox="0 0 13 8" fill="none" stroke="#222" stroke-width="1.1"><path d="M0 4h12M9 1l3 3-3 3"/></svg></li>
    <li>SHOES <svg width="13" height="8" viewBox="0 0 13 8" fill="none" stroke="#222" stroke-width="1.1"><path d="M0 4h12M9 1l3 3-3 3"/></svg></li>
    <li>FLATS <svg width="13" height="8" viewBox="0 0 13 8" fill="none" stroke="#222" stroke-width="1.1"><path d="M0 4h12M9 1l3 3-3 3"/></svg></li>
    <li>HEELS <svg width="13" height="8" viewBox="0 0 13 8" fill="none" stroke="#222" stroke-width="1.1"><path d="M0 4h12M9 1l3 3-3 3"/></svg></li>
    <li>ETHNIC <svg width="13" height="8" viewBox="0 0 13 8" fill="none" stroke="#222" stroke-width="1.1"><path d="M0 4h12M9 1l3 3-3 3"/></svg></li>
    <li>SLIPPERS <svg width="13" height="8" viewBox="0 0 13 8" fill="none" stroke="#222" stroke-width="1.1"><path d="M0 4h12M9 1l3 3-3 3"/></svg></li>
    <li>CASUALS <svg width="13" height="8" viewBox="0 0 13 8" fill="none" stroke="#222" stroke-width="1.1"><path d="M0 4h12M9 1l3 3-3 3"/></svg></li>
    <li>FORMALS <svg width="13" height="8" viewBox="0 0 13 8" fill="none" stroke="#222" stroke-width="1.1"><path d="M0 4h12M9 1l3 3-3 3"/></svg></li>
  </ul>

  <div class="pager">
    <span class="pg arrow"><svg width="10" height="14" viewBox="0 0 10 14" fill="none" stroke="#222" stroke-width="2"><path d="M8 1L2 7l6 6"/></svg></span>
    <span class="pg">1</span><span class="pg">2</span><span class="pg active">3</span><span class="pg">4</span><span class="pg">9</span>
    <span class="pg arrow"><svg width="10" height="14" viewBox="0 0 10 14" fill="none" stroke="#222" stroke-width="2"><path d="M2 1l6 6-6 6"/></svg></span>
  </div>

  <footer class="footer">
    <div class="fcol" style="left:129px">
      <h4>Let us help you</h4>
      <a>Search</a><a>About Us</a><a>Footwear Size</a><a>Care Guide</a><a>Shipping</a><a>Contact</a><a>FAQS</a>
    </div>
    <div class="fcol" style="left:365px">
      <h4>Information</h4>
      <a>Site Map</a><a>Terms &amp; Condition</a><a>Privacy Policy</a><a>FAQ's</a><a>Customer Service</a><a>Disclaimer</a>
    </div>
    <div class="fcol" style="left:588px">
      <h4>Contact Us</h4>
      <div class="contact-row"><svg width="13" height="10" viewBox="0 0 13 10"><rect width="13" height="10" rx="1" fill="var(--red)"/><path d="M0 1l6.5 5L13 1" fill="none" stroke="#fff" stroke-width="1.2"/></svg><div>Email:<br>info@example.com.au</div></div>
      <div class="contact-row"><svg width="13" height="13" viewBox="0 0 13 13" fill="none" stroke="var(--red)" stroke-width="1.5"><path d="M3 1l2 3-1.5 1.5c1 2 2 3 4 4L9 8l3 2-1 2c-5 0-10-5-10-10z"/></svg><div>Phone:<br>(+08) 123 456 7890</div></div>
      <div class="contact-row"><svg width="13" height="14" viewBox="0 0 13 14"><path d="M6.5 14S1 8.5 1 5.5a5.5 5.5 0 0111 0C12 8.5 6.5 14 6.5 14z" fill="var(--red)"/><circle cx="6.5" cy="5.5" r="2" fill="#fff"/></svg><div>Office Location:<br>Some address line goes here<br>city name</div></div>
    </div>
    <div class="fcol" style="left:850px">
      <h4>Stay Connected</h4>
      <div class="socials"><span style="background:#3b5aa8"></span><span style="background:#29a6e8"></span><span style="background:#c94a8f"></span></div>
      <h4>Payment Method</h4>
      <div class="pay">
        <span style="background:#fff;color:#333">Paywell</span>
        <span style="background:#2340b8;color:#fff">Vireo</span>
        <span style="background:#222;color:#fff">Mintcard</span>
        <span style="background:#fff;color:#333">Farpoint</span>
      </div>
    </div>
    <div class="f-rule"></div>
    <div class="copy">© COPYRIGHT 2021 - ALL RIGHTS RESERVED</div>
    <div class="totop"><svg width="10" height="13" viewBox="0 0 10 13" fill="none" stroke="#fff" stroke-width="1.3"><path d="M5 13V1M1 5l4-4 4 4"/></svg></div>
  </footer>
</div>
</body>
</html>
```